Für das Kirchenkreismusikfest wird ein Plakat gesucht
Zielgruppe
Wir sind der Kirchenkreis Lemmbrück in Niedersachsen. Ich bin der Kirchenkreiskantor (Kirchenmusiker) und veranstalte am 23. Februar ein Kirchenkreismusikfest. Dabei präsentiert sich der Kirchenkreis mit all seinen musikalischen Fassetten. Daran nehmen viele Chöre und musikalische Gruppen aus den Gemeinden im Kirchenkreis teil. Zielgruppe ist das Klient aus den Kirchengemeinden (vornehmlich im Alter von 30-70 m/w), aber für Leute, die nichts mit Kirche am Hut haben, soll das Plakat ebensbo ansprechend sein.
Aufgabenstellung
Wenn möglich, wären die Formate DIN A 3 und DIN A 2 und auch DIN A 4 gut.
Folgender Text soll berücksichtigt werden (kann sich in den nächsten Tagen auch noch mal etwas ändern):
Kirchenkreismusikfest „Mit Stimme, Klang und Freude“
Samstag, 23.2.19 in der St. Amalien-Kirche in Lemmbrück
15 Uhr Eröffnung
15.30 bis 19.00 Uhr
19 Uhr Gemeinsamer Abschluss
Dazwischen finden Kurzkonzerte im halbstündigen Abstand statt.
Das Kirchenkreismusikfest wird gestaltet von:
Projektchor „Joyful&Bright“
Bläserchor des Kirchenkreises
Kantorei St. Amalien
Gemeinsames Flötenorchester
Gospelchor Tessendorf
Organistinnen und Organisten des Kirchenkreises
Gitarrengruppe Ostermoor
und den Zuschauern selbst
Gesamtleitung: Kirchenkreiskantor Konrad Behlsen
Eintritt frei

```html
<!DOCTYPE html>
<html lang="de">
<head>
<meta charset="utf-8">
<title>Kirchenkreismusikfest – Plakat</title>
<link rel="stylesheet" href="https://fonts.googleapis.com/css2?family=Cabin+Condensed:wght@500;600;700&display=swap">
<style>
  :root {
    --purple: #7f1b60;
    --yellow: #f6bd3d;
    --paper: #efeef1;
    --stage: #c9cacd;
  }
  * { margin: 0; padding: 0; box-sizing: border-box; }
  html, body { width: 1200px; height: 848px; overflow: hidden; background: var(--stage); }
  body { font-family: "Cabin Condensed", "Arial Narrow", sans-serif; }

  .poster {
    position: absolute; left: 317px; top: 24px;
    width: 566px; height: 800px;
    background: var(--paper);
    overflow: hidden;
  }
  .band {
    position: absolute; inset: 0;
    background: var(--purple);
    clip-path: polygon(0 200px, 100% 182px, 100% 679px, 0 698px);
  }
  .placeholder { position: absolute; }
  .notes-top { left: 0; top: 14px; width: 248px; height: 100px;
    background: linear-gradient(100deg, rgba(127,27,96,.35), rgba(127,27,96,.08)); border-radius: 40px 8px 40px 8px; }
  .hand-art { left: 276px; top: 306px; width: 286px; height: 346px;
    background: radial-gradient(ellipse at 55% 55%, rgba(246,189,61,.45), rgba(246,189,61,.08) 70%); border-radius: 40% 50% 45% 55%; }
  .notes-bottom { left: 304px; top: 594px; width: 260px; height: 82px;
    background: linear-gradient(100deg, rgba(239,238,241,.08), rgba(239,238,241,.35)); border-radius: 30px 6px 30px 6px; }

  .brand {
    position: absolute; left: 222px; top: 78px;
    display: flex; align-items: center; gap: 8px;
    color: var(--purple); font-weight: 600; font-size: 21px; letter-spacing: 1.5px;
  }
  .brand-mark { width: 12px; height: 12px; background: var(--purple); }

  .title-1 {
    position: absolute; left: 30px; top: 112px;
    color: var(--purple); font-weight: 700; font-size: 74px; line-height: 1; letter-spacing: -1px;
  }
  .title-2 {
    position: absolute; left: 26px; top: 176px;
    color: var(--paper); font-weight: 700; font-size: 112px; line-height: 1; letter-spacing: -2px;
  }
  .motto {
    position: absolute; right: 46px; top: 272px;
    color: var(--paper); font-weight: 700; font-size: 25px; line-height: 1;
  }

  .tag {
    position: absolute; left: 24px;
    background: var(--yellow); color: var(--purple);
    font-weight: 700; font-size: 19px; line-height: 1; padding: 4px 6px;
  }
  .tag-program { top: 314px; }
  .tag-cast { top: 502px; }

  .program { position: absolute; left: 28px; top: 352px; list-style: none; color: var(--paper); font-weight: 500; font-size: 15px; line-height: 20px; }
  .program li { position: relative; padding-left: 11px; margin-bottom: 5px; }
  .program li::before { content: "›"; position: absolute; left: 0; }

  .cast { position: absolute; left: 26px; top: 540px; list-style: none; color: var(--paper); font-weight: 500; font-size: 15px; line-height: 21px; }
  .cast li { display: flex; gap: 10px; margin-bottom: 6px; }
  .cast-icon { width: 32px; height: 28px; margin-top: 4px; background: rgba(246,189,61,.6); border-radius: 10px; flex: none; }

  .date {
    position: absolute; left: 22px; top: 712px;
    color: var(--purple); font-weight: 700; font-size: 42px; line-height: 1; letter-spacing: -0.5px;
    transform: rotate(-1.6deg); transform-origin: left bottom; white-space: nowrap;
  }
  .venue {
    position: absolute; left: 22px; top: 768px;
    color: var(--purple); font-weight: 600; font-size: 22px; line-height: 1; white-space: nowrap;
  }
  .free {
    position: absolute; left: 370px; top: 754px;
    background: var(--purple); color: var(--yellow);
    font-weight: 700; font-size: 27px; line-height: 1; padding: 4px 8px;
    transform: rotate(-3deg);
  }
</style>
</head>
<body>
  <main class="poster">
    <div class="band"></div>

    <div class="placeholder notes-top" role="img" aria-label="Gezeichnete Notenzeilen mit Violinschlüssel und Noten"></div>

    <div class="brand"><span class="brand-mark"></span>Kirchenkreis Lemmbrück</div>

    <h1>
      <span class="title-1">KIRCHENKREIS</span>
      <span class="title-2">MUSIKFEST</span>
    </h1>
    <p class="motto">„MIT STIMME, KLANG UND FREUDE“</p>

    <div class="placeholder hand-art" role="img" aria-label="Gelbe Linienzeichnung: Hand mit Herz und Mund"></div>

    <h2 class="tag tag-program">PROGRAMM</h2>
    <ul class="program">
      <li>15.00 Uhr<br>Eröffnung</li>
      <li>15.30 bis 19.00 Uhr<br>Kurzkonzerte in halbstündigem Abstand</li>
      <li>19.00 Uhr<br>Gemeinsamer Abschluss</li>
    </ul>

    <h2 class="tag tag-cast">MITWIRKENDE</h2>
    <ul class="cast">
      <li><span class="cast-icon" role="img" aria-label="Kleines Stimme-Symbol"></span><span>Mit Stimme:<br>Alle 200 Beteiligten</span></li>
      <li><span class="cast-icon" role="img" aria-label="Kleines Klang-Symbol"></span><span>Klang:<br>Projektchor, Kantorei, Gospelchor</span></li>
      <li><span class="cast-icon" role="img" aria-label="Kleines Freude-Symbol"></span><span>und Freude:<br>Blechbläser, Organisten, Flötenorchester</span></li>
    </ul>

    <div class="placeholder notes-bottom" role="img" aria-label="Gezeichnete Notenzeilen mit Noten"></div>

    <p class="date">SAMSTAG, 23. FEBRUAR 2019</p>
    <p class="venue">in der St. Amalien-Kirche in Lemmbrück</p>
    <p class="free">EINTRITT FREI</p>
  </main>
</body>
</html>
```